依頼詳細
シニア向け通販媒体にて展開するA5サイズ片面カラーのチラシの作成を依頼致します。年配者の女性をターゲットにしていますので、読みやすく、安心感がありかつ雰囲気のあるデザインを期待致します。
記載項目
詳しくは添付の指示書、画像をご確認をお願い申し上げます。
サイズ
A5
ページ数
片面
希望イメージ
• +5 0 +5
• シンプル
複雑
• 単色
カラフル
• 暗い
明るい
• 日常
高級
• 遊び心
厳粛
• 未来的
伝統的
• 女性的
男性的
希望する色
赤系、黄・オレンジ系
納品ファイル
• イラストレーター形式 (.ai)
補足説明
依頼公開後の追記内容
申込書は別紙になりますので、会社名や申し込み方法や電話番号の記載は必要ございません。
パッケージ画像は1袋のみの掲載でお願い申し上げます。
■ 選んだ理由

インパクトがあり雰囲気もよく何より干しいもが美味しそうに見えるので採用させていただきました。

■ 提案者全員のお礼・コメント

皆様、たくさんの素晴らしいご提案をありがとうございます。
どのデザインも素晴らしくとても悩みました。
また機会がございましたらよろしくお願いいたします。

```html
<!DOCTYPE html>
<html lang="ja">
<head>
<meta charset="utf-8">
<title>ほっこり干しいも雅 チラシ</title>
<link href="https://fonts.googleapis.com/css2?family=Shippori+Mincho+B1:wght@500;700;800&family=Noto+Sans+JP:wght@500;700&display=swap" rel="stylesheet">
<style>
:root{
  --paper:#fbf7f1;
  --purple:#6e2465;
  --purple-deep:#4f1549;
  --ink:#2b1a14;
  --orange:#e07a12;
  --amber:#f3a51d;
  --yellow:#ffe36a;
  --potato:#f0a535;
  --potato-light:#fbd27a;
  --white:#ffffff;
}
*{margin:0;padding:0;box-sizing:border-box}
html,body{width:844px;height:1200px;overflow:hidden;background:var(--paper)}
.flyer{position:relative;width:844px;height:1200px;overflow:hidden;background:var(--paper);font-family:"Shippori Mincho B1",serif;color:var(--ink)}
.vertical{writing-mode:vertical-rl;text-orientation:upright;position:absolute;white-space:nowrap}
.photo-senior{position:absolute;left:450px;top:0;width:262px;height:337px;background:linear-gradient(160deg,#e9ddd3,#cbb7a8 60%,#b79c8a)}
.photo-potatoes{position:absolute;left:155px;top:205px;width:265px;height:132px;background:radial-gradient(ellipse at 50% 55%,#b04a5c,#8a2f45 55%,#e9e0d8 85%);border-radius:8px}
.photo-hoshiimo{position:absolute;left:0;top:365px;width:844px;height:535px;background:radial-gradient(ellipse at 55% 50%,var(--potato-light),var(--potato) 45%,#d47d1c 68%,rgba(251,247,241,0) 78%)}
.intro{position:absolute;left:152px;top:18px;width:290px}
.intro-label{display:inline-block;background:var(--purple);color:var(--white);font-size:17px;padding:2px 6px;font-weight:700}
.intro-title{color:var(--purple);font-size:24px;font-weight:800;margin:4px 0 6px;line-height:1.2}
.intro-text{font-family:"Noto Sans JP",sans-serif;font-size:11px;line-height:1.6;color:var(--ink)}
.headline-soft{left:8px;top:12px;font-size:112px;font-weight:800;color:var(--purple);line-height:1;letter-spacing:-6px}
.headline-sweet{right:6px;top:0;font-size:104px;font-weight:800;color:var(--ink);line-height:1;letter-spacing:-4px}
.headline-sweet .accent{color:var(--orange)}
.tagline{left:518px;top:300px;width:70px;height:335px;background:var(--purple);color:var(--white);font-size:44px;font-weight:800;display:flex;align-items:center;justify-content:center;line-height:70px}
.badge{position:absolute;width:94px;height:94px;border-radius:50%;background:var(--orange);color:var(--white);font-size:22px;font-weight:800;display:flex;align-items:center;justify-content:center;border:3px solid var(--white);box-shadow:0 2px 4px rgba(0,0,0,.2);z-index:2}
.badge--additive{left:232px;top:668px}
.badge--colour{left:340px;top:668px}
.amount{position:absolute;left:680px;top:680px;width:150px;height:150px;border-radius:50%;background:var(--amber);color:var(--white);display:flex;flex-direction:column;align-items:center;justify-content:center;border:3px solid var(--white);box-shadow:0 2px 4px rgba(0,0,0,.2);z-index:2}
.amount-lead{font-size:22px;font-weight:700}
.amount-value{font-size:52px;font-weight:800;line-height:1}
.amount-value small{font-size:22px}
.offer{position:absolute;left:337px;top:905px;width:507px;height:295px;background:linear-gradient(180deg,var(--purple),var(--purple-deep));color:var(--white);padding:26px 20px 0 30px}
.product-name{font-size:33px;font-weight:800;letter-spacing:1px}
.product-spec{font-size:17px;margin:6px 0 24px;font-weight:700}
.price-line{font-family:"Noto Sans JP",sans-serif;font-size:16px;font-weight:700;margin-bottom:10px;white-space:nowrap}
.price-line em{font-style:normal;color:var(--yellow);font-size:22px}
.package{position:absolute;left:56px;top:730px;width:281px;height:450px;background:linear-gradient(180deg,#f6f1ea,#f4c77a 55%,#e99a2c);border-radius:10px 10px 6px 6px;box-shadow:0 3px 8px rgba(0,0,0,.25);z-index:1}
</style>
</head>
<body>
<main class="flyer">
  <div class="photo-hoshiimo" role="img" aria-label="黄金色のやわらかな干しいもの写真"></div>
  <div class="photo-senior" role="img" aria-label="干しいもを手に微笑むシニア女性の写真"></div>
  <div class="photo-potatoes" role="img" aria-label="紅はるかのさつまいもの写真"></div>

  <section class="intro">
    <span class="intro-label">茨城県産</span>
    <p class="intro-title">「紅はるか」使用</p>
    <p class="intro-text">「紅はるか」は蜜芋とよばれるほど糖度が高く、やわらかい食感が特徴です。その他の干しいもは食べられなくなるほど美味しい「ほっこり干しいも雅」を是非この機会にお試しください！</p>
  </section>

  <h1 class="vertical headline-soft">「やわらかさ」</h1>
  <p class="vertical headline-sweet">驚きの「<span class="accent">甘さ</span>」と</p>
  <p class="vertical tagline">絶品干しいも</p>

  <div class="badge badge--additive">無添加</div>
  <div class="badge badge--colour">無着色</div>

  <div class="amount">
    <span class="amount-lead">たっぷり</span>
    <span class="amount-value">200<small>g</small></span>
  </div>

  <div class="package" role="img" aria-label="ほっこり干しいも雅のパッケージ写真"></div>

  <section class="offer">
    <h2 class="product-name">ほっこり干しいも雅</h2>
    <p class="product-spec">原材料:さつまいも(茨城県産) 賞味期限:45日</p>
    <p class="price-line">1袋:本体価格<em>978円</em>(税込1,056円)</p>
    <p class="price-line">お買い得2袋セット:本体価格<em>1,856円</em>(税込2,004円)</p>
  </section>
</main>
</body>
</html>
```